Relaunch website sonnenundrhein.de

We are looking for creative minds to relaunch the website for our award-winning comedy musical “Wolken und Brise” (www.sonnenundrhein.de). The aim is a cheeky, funny and surprising website that underlines our position as “Germany's funniest musical” and motivates people to buy tickets. The site should convey the positive Cologne attitude to life, be responsive and offer intuitive navigation.

Design specifications: Magenta-purple as the main color with golden accents. Font: Bebas Neue for headlines, Open Sans Condensed for body text.
The heart logo is to be placed at the top left. Various key visuals such as a drawn Cologne skyline or other drawings etc. should be integrated.

In addition to the main page, the subpages: The Musical, Ticket Info, Plan a Visit, Company Events are to be created.

The winner will be selected according to the following criteria: Creativity, user guidance, technical feasibility and compliance with the style guide.

I have uploaded briefing documents in English If you have any questions, please contact lukas.brandt@veltora-buehne.

Further briefings and the style guide have been uploaded in the appendix.

Additionally, graphics can be downloaded under these links (the download of the files takes longer):

http://VELTORA-NAS.fernlager.example/d/s/12hIMn5Y8tBxruv0eqvaTYrfzCXX1ZXE/W2t9gugGTtFgGl2YAyfn0qzz0Jvma2EO-j7YglkhkKww

Link LOGO:
http://VELTORA-NAS.fernlager.example/d/s/12hzRrDEelalG3eIQ1zqq10t7HylrWfW/Y4BTw-kx2bB6SC1pgNFkVCuC0_7yzXY5-XLpAKylVKww

http://VELTORA-NAS.fernlager.example/d/s/12lNTwd0im1cftcjvYC45mULZ0Fh0YTU/rlBvu8wD4UG6w7gLlYP8xqw2kmzaoiy1-H7sAETBWKww

Target Market(s)

Germany-wide + region 40 kilometers around Cologne

Industry/Entity Type

Entertaunment Produktion

Coding

Coded - Design and coding required

Number of Pages Required

4 page

Font styles to use
Other font styles liked:
• Bebas Neue , Open Sans Condensed

Colors
E54698
E96AAD
F1A4CE
F9D9EA
FCEFF6
A7469A
B969AE
D3A5CF
EDDBEB
F8F0F9

Requirements
Must have
• Color scheme • Main color: magenta-violet • Accent color: gold/gold tones • Complementary colors: shades of the main color and neutral tones for body text Typography • Headlines: Bebas Neue (sans-serif, no italics or small capitals) • Copy texts: Open Sans Condensed (all styles allowed, no italics) • Clear hierarchy for optimal readability and recognition Logo • The heart logo must always appear on a heart-shaped background • Variants with the addition "The Cologne Musical" are possible • Prominent placement in all areas of the website Key visuals • Combination of striking illustrations with local Cologne symbols • Cologne skyline with cathedral and TV tower • Golden accents and rainbow elements • Kölsch glass as a local reference • Stylized graphic elements in gold (stars, glitter effects, frames) Website structure and content Header area • Dynamic news ticker with current offers and performance dates • Logo (left) and main navigation (right) • Prominently placed "Get Tickets" button in gold • Main menu items: Musical, Ticket Info, Plan Visit, Groups, Corporate Events, FAQ Hero Section • Emotionally effective video background or changing key visuals • Concise headline: "WOLKEN UND BRISE - The award-winning Cologne musical" • Subheadline with a special humorous component • Eye-catching CTA button "GET TICKETS" with price information Celebrity Endorsement Section • Creative slider concept with testimonials from well-known personalities • Integration of quotes from Marlene Oswitz, Reinhard Plomberg, Dieter Hanslik • Authentic representation of the celebrities in connection with the musical Awards & Headlines • Visual highlighting of the awards • Infographic on visitor numbers (144. 000+) and recommendation rate • Integration of the four German musical and theater awards as badges/icons Show description • Humorous presentation of the plot surrounding Pastor Gunnar • Creative visualization of the show highlights • List of special features (live orchestra, choreography, etc. ) • Integration of Cologne local flavor Press reviews slider • Dynamic concept for presenting press reviews • Integration of quotes from Blatt zum Montag, Kurier, Rheinische Morgenpost • Visual linking with the respective media logos Highlight scenes • Interactive photo gallery with short, witty descriptions • Potential integration of short video snippets • "Appetizers" without giving too much away about the musical USP section • Four concise icons with accompanying text • Highlighting the unique selling points: live orchestra, unique venue, sustainability, Cologne culture • Creative implementation of the icons in the style of the musical Voucher banner • Eye-catching design for the voucher area • Emotional appeal: "Give the gift of unforgettable moments" • Direct CTA for voucher ordering Visitor comments • Authentic testimonials with real visitor photos • Representation of various target group representatives • Integration of "people next door" perspectives Experience Cologne banner • Linking the musical with Cologne sights • Communicating the "Cologne experience" • Strong CTA for ticket booking Corporate events section • Presentation of business offers • Showcasing the possible combinations of business and pleasure • Presentation of VIP packages and special arrangements Quick links • Six attractively designed image tiles • Intuitive navigation to important subsections • Subject areas: Arrival & parking, ticket categories, performance times, corporate events, group offers, FAQ Footer area • Newsletter registration with emotional incentive • Clear contact information • Social media integration (Frendly, Pixaroo, Vidplex, Flipzy) • Area for legal information Functional requirements Responsive design • Optimal display on all devices (desktop, tablet, smartphone) • Special attention to mobile-first approach Performance • Fast loading times despite multimedia content • Optimization of all images and videos SEO optimization • SEO-friendly URL structure • Meta information for all pages • Semantic HTML structure • Keyword optimization for "Musical Cologne", "Comedy Musical", etc. • Special requirements for the wireframe Tonality and creativity The wireframe should already convey the cheeky, witty tone of the musical. Look for surprising elements that make you smile and capture the Cologne way of life. Integrate Cologne humor into UI elements, navigation terms, or micro-interactions. User path to ticket purchase Show how you can guide the user to ticket purchase through clever UX design. Pay particular attention to: • Strategic placement of calls to action • Reducing click paths to ticket purchases • Emotional triggers at decision points Surprising interaction elements Design unusual interaction elements that fit the character of the musical: • Cologne Cathedral that "sings" on hover • Interactive Cologne city scenes • Humorous loading animations • Easter eggs that appeal to Cologne insider knowledge Multi-device concept Show how your ideas work on different devices. Particularly important: • How navigation works on mobile devices • How complex elements like the seating plan are displayed on small screens • Which content is prioritized on mobile
Nice to have
• See briefing

```html
<!DOCTYPE html>
<html lang="en">
<head>
<meta charset="utf-8">
<title>Wolken und Brise – Web Design</title>
<link rel="stylesheet" href="https://fonts.googleapis.com/css2?family=Bebas+Neue&family=Oswald:wght@300;400;500;600&family=Montserrat:wght@500;700&family=Poppins:wght@700&display=swap">
<style>
:root{
  --magenta:#e218a9;
  --magenta-deep:#b8148c;
  --gold:#fcb900;
  --gold-soft:#ffe9a8;
  --blush:#fde1f2;
  --blush-line:#f3a6d4;
  --night:#231a3e;
  --navy:#17099e;
  --ink:#2b2b2b;
  --grey:#8a8a8a;
  --white:#ffffff;
  --black:#000000;
}
*{box-sizing:border-box;margin:0;padding:0}
html,body{width:1200px;height:1200px;overflow:hidden;background:var(--black)}
.board{position:absolute;left:0;top:0;width:1932px;height:1932px;transform:scale(.62112);transform-origin:0 0;background:var(--black);font-family:"Oswald",sans-serif}
.a{position:absolute}
.board-title{left:262px;top:6px;font-family:"Poppins",sans-serif;font-weight:700;font-size:92px;color:var(--white);letter-spacing:2px}
.page{position:absolute;top:137px;width:556px;height:1749px;background:var(--white);overflow:hidden}
.bebas{font-family:"Bebas Neue",sans-serif;font-weight:400}
.center{text-align:center}
.gold{color:var(--gold)}
.white{color:var(--white)}
.band{background:var(--magenta)}
.btn-outline{border:1.5px solid var(--gold);color:var(--gold);font-family:"Bebas Neue",sans-serif;font-size:14px;letter-spacing:.5px;display:flex;align-items:center;justify-content:center;gap:8px;border-radius:2px}
.btn-outline svg{width:14px;height:8px}
.photo{border-radius:6px}
/* header */
.ticker{left:0;top:0;width:556px;height:20px;background:var(--magenta);color:var(--white);font-size:6px;white-space:nowrap;line-height:20px;overflow:hidden}
.ticker b{color:var(--gold);font-size:12px;margin:0 8px;vertical-align:middle}
.brand-mark{left:14px;top:27px;font-family:"Bebas Neue",sans-serif;font-size:10px;line-height:10px;color:#e2262e;width:44px;text-align:center}
.nav{left:71px;top:30px;display:flex;gap:10px;font-family:"Oswald",sans-serif;font-weight:500;font-size:7.5px;color:var(--ink)}
.nav .active{color:var(--magenta)}
.nav-cta{left:434px;top:23px;width:103px;height:27px;background:var(--magenta);color:var(--gold);font-family:"Bebas Neue",sans-serif;font-size:13px;display:flex;align-items:center;justify-content:center;gap:6px}
/* ticket card */
.ticket{position:absolute;left:35px;width:487px;height:152px;background:var(--white);border-radius:8px}
.ticket::before,.ticket::after{content:"";position:absolute;top:56px;width:40px;height:52px;border-radius:50%;background:var(--magenta)}
.ticket::before{left:-26px}
.ticket::after{right:-26px}
.t-day{left:15px;top:8px;width:35px;height:136px;background:var(--gold);display:flex;align-items:center;justify-content:center}
.t-day span{transform:rotate(-90deg);font-family:"Bebas Neue",sans-serif;font-size:20px;color:var(--magenta);white-space:nowrap}
.t-note{left:59px;top:10px;width:259px;height:28px;background:var(--blush);border:1px solid var(--blush-line);border-radius:3px;padding:3px 5px;font-size:5px;color:var(--magenta);line-height:7px}
.t-note b{display:block;color:var(--ink);font-weight:600}
.t-select{top:58px;height:34px;border:1px solid var(--gold-soft);background:#fffaf0;border-radius:3px;color:var(--gold);font-size:9px;display:flex;align-items:center;justify-content:center;gap:4px}
.t-label{left:59px;top:111px;font-size:5.5px;color:var(--ink);font-weight:500}
.chip{top:126px;height:14px;border:1px solid var(--gold);border-radius:2px;font-size:5px;color:var(--gold);display:flex;align-items:center;justify-content:center}
.chip.on{background:var(--gold);color:var(--white)}
.t-sep{left:329px;top:10px;height:135px;border-left:1.5px dashed #b9b9b9}
.t-pack{left:339px;top:14px;font-family:"Bebas Neue",sans-serif;font-size:13px;color:var(--grey)}
.t-chev{left:453px;top:17px;width:8px;height:6px}
.t-price{left:339px;top:40px;font-family:"Bebas Neue",sans-serif;font-size:19px;color:var(--gold)}
.t-price small{font-size:12px;color:var(--grey)}
.t-qty{left:425px;top:46px;display:flex;align-items:center;gap:6px;font-size:8px;font-weight:600;color:var(--ink)}
.t-qty i{width:8px;height:8px;border-radius:50%;background:var(--gold)}
.t-qty i.plus{background:#ff8a3d}
.t-row{left:339px;width:121px;display:flex;justify-content:space-between;font-size:5px;color:var(--grey)}
.t-row.total{color:var(--ink);font-weight:600}
.t-row .v{color:var(--gold)}
.t-buy{left:339px;top:114px;width:120px;height:27px;background:var(--gold);color:var(--magenta);font-family:"Bebas Neue",sans-serif;font-size:12px;display:flex;align-items:center;justify-content:center}
/* contact */
.c-icon{width:13px;height:13px;stroke:var(--grey);fill:none;stroke-width:1.4}
.c-label{font-size:7px;font-weight:600;color:var(--ink);font-family:"Montserrat",sans-serif}
.c-value{font-size:10px;color:var(--ink);font-family:"Montserrat",sans-serif;font-weight:500}
/* faq */
.faq-row{left:35px;width:486px;height:36px;border:1px solid rgba(252,185,0,.55);border-radius:3px;color:var(--gold);font-family:"Bebas Neue",sans-serif;font-size:11px;display:flex;align-items:center;justify-content:space-between;padding:0 10px}
.faq-row.open{background:var(--gold);color:var(--white);border-color:var(--gold)}
.faq-row svg{width:7px;height:5px}
/* footer */
.f-icon{width:14px;height:14px;stroke:var(--white);fill:none;stroke-width:1.4}
.f-label{font-size:7px;color:var(--white);font-family:"Montserrat",sans-serif;font-weight:700}
.f-value{font-size:9.5px;color:var(--white);font-family:"Montserrat",sans-serif;font-weight:500}
.f-links{font-family:"Montserrat",sans-serif;color:var(--white);font-size:5px;line-height:16px}
.f-links b{display:block;font-size:7px;margin-bottom:4px}
.ring{fill:none;stroke:var(--gold);stroke-width:8}
</style>
</head>
<body>
<div class="board">
  <div class="a board-title">web design</div>

  <!-- PAGE 1: ticket info top -->
  <section class="page" style="left:172px">
    <div class="a ticker">ats now! ++ <b>✳</b> ++ NEW: VIP packages now available ++ Special offer: 20% discount for groups of 8 or more ++ Next show: [Date] - Secure the best seats now! ++ <b>✳</b> ++ NEW: VIP packages now</div>
    <div class="a brand-mark">Wolken und Brise</div>
    <nav class="a nav"><span>HOME</span><span>DAS MUSICAL</span><span class="active">TICKETINFORMATIONEN</span><span>PLANEN SIE EINEN BESUCH</span><span>FIRMENVERANSTALTUNGEN</span><span>FAQ</span></nav>
    <div class="a nav-cta">TICKETS KAUFEN <svg width="12" height="6" viewBox="0 0 12 6"><path d="M0 3h11M8 0l3 3-3 3" stroke="currentColor" fill="none"/></svg></div>

    <div class="a band" style="left:16px;top:169px;width:525px;height:494px"></div>
    <div class="a photo" role="img" aria-label="Theatre auditorium with audience, tinted magenta" style="left:38px;top:66px;width:482px;height:269px;background:linear-gradient(180deg,#e86fc3 0%,#c63ea0 55%,#8d2a77 100%)"></div>
    <h1 class="a bebas gold center" style="left:38px;top:170px;width:482px;font-size:52px;line-height:52px">SECURE THE BEST SEATS!</h1>
    <h2 class="a bebas gold center" style="left:38px;top:357px;width:482px;font-size:41px;line-height:38.5px">YOUR GATEWAY TO AN UNFORGETTABLE MUSICAL EXPERIENCE – CONVENIENT, FAST, AND SECURE!</h2>
    <p class="a white center" style="left:30px;top:516px;width:497px;font-size:15px;line-height:17px;font-weight:500;text-transform:uppercase">Everything you need to know for your visit to Wolken und Brise: showtimes, prices, discounts, and more.</p>
    <div class="a btn-outline" style="left:217px;top:592px;width:122px;height:33px">BUY TICKETS NOW <svg viewBox="0 0 14 8"><path d="M0 4h13M10 1l3 3-3 3" stroke="currentColor" fill="none"/></svg></div>

    <div class="a band" style="left:16px;top:788px;width:525px;height:961px"></div>
    <div class="a photo" style="left:38px;top:684px;width:482px;height:250px;background:linear-gradient(180deg,#d01aa0 0%,#7a1a73 55%,#261b3e 100%)"></div>
    <h2 class="a bebas gold center" style="left:38px;top:718px;width:482px;font-size:60px;line-height:58px">OUR PRICES – THE RIGHT TICKET FOR EVERYONE</h2>
    <p class="a white center" style="left:38px;top:980px;width:482px;font-size:13.5px;line-height:18px;font-weight:300">Wolken und Brise offers the perfect category for every budget. Enjoy the musical from exclusive PK1 balcony seats or choose our affordable options for an unforgettable evening at Cologne's most beautiful venue.</p>
    <h3 class="a bebas white center" style="left:16px;top:1053px;width:525px;font-size:31px">OUR SCHEDULE – PLAN YOUR VISIT</h3>
    <p class="a white center" style="left:16px;top:1100px;width:525px;font-size:12.5px;font-weight:300">Come and be amazed: Wolken und Brise plays four days a week. Choose the show that fits perfectly into your schedule.</p>

    <div class="ticket" style="top:1133px">
      <div class="a t-day"><span>DONNERSTAG</span></div>
      <div class="a t-note"><b>N.B.</b>Our PK1 balcony seats offer the best view of the stage, paired with exclusive perks like private restrooms on the first floor.</div>
      <div class="a t-select" style="left:59px;width:119px">7 JAN 2025 ⌄</div>
      <div class="a t-select" style="left:193px;width:125px">3:00 PM ⌄</div>
      <div class="a t-label">Exclusive Discounts for Students, Seniors, and People with Disabilities**</div>
      <div class="a chip" style="left:59px;width:56px">SENIOR DISCOUNT 8%</div>
      <div class="a chip on" style="left:152px;width:60px">STUDENT DISCOUNT 8%</div>
      <div class="a chip" style="left:250px;width:66px">DISABILITY DISCOUNT 25%</div>
      <div class="a t-sep"></div>
      <div class="a t-pack">PACKAGE 1</div>
      <svg class="a t-chev" viewBox="0 0 8 6"><path d="M1 1l3 3 3-3" stroke="#999" fill="none"/></svg>
      <div class="a t-price">€84.90<small>/PERSON</small></div>
      <div class="a t-qty"><i></i>2<i class="plus"></i></div>
      <div class="a t-row" style="top:78px"><span>Discount Total</span><span>-€20</span></div>
      <div class="a t-row total" style="top:93px"><span>Total Payment</span><span class="v">€64.90</span></div>
      <div class="a t-buy">TICKETS KAUFEN</div>
    </div>
    <div class="ticket" style="top:1295px">
      <div class="a t-day"><span>FREITAG</span></div>
      <div class="a t-note"><b>N.B.</b>Our PK1 balcony seats offer the best view of the stage, paired with exclusive perks like private restrooms on the first floor.</div>
      <div class="a t-select" style="left:59px;width:119px">8 JAN 2025 ⌄</div>
      <div class="a t-select" style="left:193px;width:125px">3:00 PM ⌄</div>
      <div class="a t-label">Exclusive Discounts for Students, Seniors, and People with Disabilities**</div>
      <div class="a chip" style="left:59px;width:56px">SENIOR DISCOUNT 8%</div>
      <div class="a chip" style="left:152px;width:60px">STUDENT DISCOUNT 8%</div>
      <div class="a chip" style="left:250px;width:66px">DISABILITY DISCOUNT 25%</div>
      <div class="a t-sep"></div>
      <div class="a t-pack">PACKAGE 2</div>
      <svg class="a t-chev" viewBox="0 0 8 6"><path d="M1 1l3 3 3-3" stroke="#999" fill="none"/></svg>
      <div class="a t-price">€79.90<small>/PERSON</small></div>
      <div class="a t-qty"><i></i>2<i class="plus"></i></div>
      <div class="a t-row" style="top:78px"><span>Discount Total</span><span>-€20</span></div>
      <div class="a t-row total" style="top:93px"><span>Total Payment</span><span class="v">€64.90</span></div>
      <div class="a t-buy">TICKETS KAUFEN</div>
    </div>
    <div class="ticket" style="top:1457px">
      <div class="a t-day"><span>SAMSTAG</span></div>
      <div class="a t-note"><b>N.B.</b>Our PK1 balcony seats offer the best view of the stage, paired with exclusive perks like private restrooms on the first floor.</div>
      <div class="a t-select" style="left:59px;width:119px">9 JAN 2025 ⌄</div>
      <div class="a t-select" style="left:193px;width:125px">7:00 PM ⌄</div>
      <div class="a t-label">Exclusive Discounts for Students, Seniors, and People with Disabilities**</div>
      <div class="a chip" style="left:59px;width:56px">SENIOR DISCOUNT 8%</div>
      <div class="a chip" style="left:152px;width:60px">STUDENT DISCOUNT 8%</div>
      <div class="a chip" style="left:250px;width:66px">DISABILITY DISCOUNT 25%</div>
      <div class="a t-sep"></div>
      <div class="a t-pack">PACKAGE 1</div>
      <svg class="a t-chev" viewBox="0 0 8 6"><path d="M1 1l3 3 3-3" stroke="#999" fill="none"/></svg>
      <div class="a t-price">€84.90<small>/PERSON</small></div>
      <div class="a t-qty"><i></i>2<i class="plus"></i></div>
      <div class="a t-row" style="top:78px"><span>Discount Total</span><span>-€20</span></div>
      <div class="a t-row total" style="top:93px"><span>Total Payment</span><span class="v">€64.90</span></div>
      <div class="a t-buy">TICKETS KAUFEN</div>
    </div>
    <div class="ticket" style="top:1618px">
      <div class="a t-day"><span>SONNTAG</span></div>
      <div class="a t-note"><b>N.B.</b>Our PK1 balcony seats offer the best view of the stage, paired with exclusive perks like private restrooms on the first floor.</div>
      <div class="a t-select" style="left:59px;width:119px">10 JAN 2025 ⌄</div>
      <div class="a t-select" style="left:193px;width:125px">7:00 PM ⌄</div>
      <div class="a t-label">Exclusive Discounts for Students, Seniors, and People with Disabilities**</div>
      <div class="a chip" style="left:59px;width:56px">SENIOR DISCOUNT 8%</div>
      <div class="a chip" style="left:152px;width:60px">STUDENT DISCOUNT 8%</div>
      <div class="a chip" style="left:250px;width:66px">DISABILITY DISCOUNT 25%</div>
      <div class="a t-sep"></div>
      <div class="a t-pack">PACKAGE 1</div>
      <svg class="a t-chev" viewBox="0 0 8 6"><path d="M1 1l3 3 3-3" stroke="#999" fill="none"/></svg>
      <div class="a t-price">€84.90<small>/PERSON</small></div>
      <div class="a t-qty"><i></i>2<i class="plus"></i></div>
      <div class="a t-row" style="top:78px"><span>Discount Total</span><span>-€20</span></div>
      <div class="a t-row total" style="top:93px"><span>Total Payment</span><span class="v">€64.90</span></div>
      <div class="a t-buy">TICKETS KAUFEN</div>
    </div>
  </section>

  <!-- PAGE 2: groups, social ticket, vouchers, club -->
  <section class="page" style="left:746px">
    <div class="a band" style="left:16px;top:0;width:525px;height:87px"></div>
    <div class="a" style="left:38px;top:-12px;width:482px;height:32px;background:var(--white);border-radius:0 0 8px 8px"></div>
    <div class="a" style="left:50px;top:-4px;width:34px;height:18px;background:var(--gold)"></div>
    <div class="a chip" style="left:96px;top:-2px;width:60px;height:10px">SENIOR DISCOUNT 8%</div>
    <div class="a chip" style="left:188px;top:-2px;width:60px;height:10px">STUDENT DISCOUNT 8%</div>
    <div class="a chip" style="left:286px;top:-2px;width:66px;height:10px">DISABILITY DISCOUNT 25%</div>
    <div class="a" style="left:364px;top:0;height:14px;border-left:1.5px dashed #b9b9b9"></div>
    <div class="a" style="left:375px;top:0;width:120px;height:10px;background:var(--gold)"></div>
    <p class="a white center" style="left:16px;top:38px;width:525px;font-size:7.5px;font-weight:500">Seniors / Students / Disabled: Please bring appropriate proof with you when attending the show; without it, we will ask you to pay the difference.</p>

    <div class="a" style="left:16px;top:106px;width:525px;height:327px;background:var(--blush)"></div>
    <h2 class="a bebas gold center" style="left:16px;top:124px;width:525px;font-size:31px;line-height:33px">EXPERIENCE WOLKEN UND BRISE TOGETHER – GROUP<br>DISCOUNTS FOR FAMILIES, FRIENDS, OR COLLEAGUES.</h2>
    <p class="a gold center" style="left:16px;top:200px;width:525px;font-size:9px;font-weight:500;text-transform:uppercase">For groups of 8 or more, we offer attractive discounts and easy booking processes. Request your group offer today!</p>
    <p class="a center" style="left:16px;top:225px;width:525px;font-size:9.5px;font-weight:300;color:var(--magenta)">FROM 8 PEOPLE: 10% DISCOUNT | FROM 16 PEOPLE: 15% DISCOUNT | FROM 25 PEOPLE: 20% DISCOUNT</p>
    <div class="a" role="img" aria-label="Portrait photo of the head of sales" style="left:24px;top:260px;width:126px;height:146px;background:linear-gradient(160deg,#3a3a3a,#9a8a80 60%,#c9d3df)"></div>
    <div class="a bebas" style="left:169px;top:257px;font-size:20px;color:var(--ink)">JONAS VELTEN</div>
    <div class="a" style="left:169px;top:281px;font-size:11px;font-weight:300;color:#666">Head of Sales and Marketing</div>
    <svg class="a c-icon" style="left:171px;top:312px" viewBox="0 0 14 14"><path d="M3 1h3l1 3-2 1a7 7 0 0 0 4 4l1-2 3 1v3a1 1 0 0 1-1 1A11 11 0 0 1 2 2a1 1 0 0 1 1-1z"/></svg>
    <div class="a c-label" style="left:195px;top:306px">Contact</div>
    <div class="a c-value" style="left:195px;top:318px">(123) 555-0147</div>
    <svg class="a c-icon" style="left:171px;top:351px" viewBox="0 0 14 14"><rect x="1" y="3" width="12" height="8"/><path d="M1 3l6 5 6-5"/></svg>
    <div class="a c-label" style="left:195px;top:345px">E-mail</div>
    <div class="a c-value" style="left:195px;top:357px">events@sonnenundrhein.de</div>
    <svg class="a c-icon" style="left:171px;top:390px" viewBox="0 0 14 14"><circle cx="7" cy="7" r="6"/><path d="M7 3v4l3 2"/></svg>
    <div class="a c-label" style="left:195px;top:384px">Available</div>
    <div class="a c-value" style="left:195px;top:396px">Monday–Friday: 9:00 AM–5:00 PM</div>

    <div class="a band" style="left:16px;top:558px;width:525px;height:377px"></div>
    <div class="a photo" style="left:38px;top:454px;width:482px;height:248px;background:linear-gradient(180deg,#d01aa0 0%,#6e1a6e 55%,#211b3c 100%)"></div>
    <div class="a bebas white center" style="left:38px;top:489px;width:482px;font-size:15px">NEW: THE SOCIAL TICKET</div>
    <h2 class="a bebas gold center" style="left:38px;top:510px;width:482px;font-size:47px;line-height:46px">CULTURE FOR EVERYONE –<br>OUR NEW SOCIAL TICKET</h2>
    <p class="a white center" style="left:100px;top:615px;width:358px;font-size:11.5px;line-height:16px;font-weight:500">At Wolken und Brise, we want everyone to have the opportunity to experience this unique musical. With our Social Ticket, we support individuals with limited budgets, making culture accessible for all!</p>
    <h3 class="a bebas white center" style="left:16px;top:747px;width:525px;font-size:23px">WHO IS ELIGIBLE FOR THE SOCIAL TICKET?</h3>
    <ul class="a white" style="left:70px;top:784px;font-size:11.5px;line-height:22px;font-weight:500">
      <li>Citizens receiving basic income support (Bürgergeld)</li>
      <li>People receiving government assistance</li>
      <li>Individuals with limited financial means</li>
    </ul>
    <p class="a white center" style="left:16px;top:887px;width:525px;font-size:7.5px;font-weight:500">Note: We trust that you will use this ticket responsibly and only claim it if you are unable to pay the regular price.</p>

    <div class="a band" style="left:16px;top:1061px;width:525px;height:383px"></div>
    <div class="a photo" role="img" aria-label="Audience in red theatre seats watching the show" style="left:38px;top:957px;width:482px;height:282px;background:linear-gradient(135deg,#c8102e 0%,#3a1a22 22%,#24181c 70%,#c8102e 100%)"></div>
    <h2 class="a bebas white" style="left:89px;top:990px;font-size:57px;line-height:54px">GIVE<br>UNFORGETTABLE<br>MOMENTS</h2>
    <p class="a white" style="left:89px;top:1151px;font-size:21px;font-weight:300">Musical gift vouchers – the perfect gift for any occasion</p>
    <svg class="a" style="left:117px;top:1176px" width="60" height="60" viewBox="0 0 60 60"><circle class="ring" cx="30" cy="30" r="24"/></svg>
    <div class="a btn-outline" style="left:220px;top:1273px;width:116px;height:34px">ORDER VOUCHER <svg viewBox="0 0 14 8"><path d="M0 4h13M10 1l3 3-3 3" stroke="currentColor" fill="none"/></svg></div>
    <h3 class="a bebas white center" style="left:16px;top:1342px;width:525px;font-size:21px">GIVE MAGICAL MOMENTS</h3>
    <p class="a white center" style="left:38px;top:1372px;width:482px;font-size:12.5px;line-height:17px;font-weight:300">Looking for the perfect gift for your loved ones? Whether for birthdays, Christmas, or Valentine's Day – a gift voucher for Wolken und Brise creates unforgettable memories.</p>

    <div class="a band" style="left:16px;top:1608px;width:525px;height:141px"></div>
    <div class="a photo" role="img" aria-label="Purple starry sky with light beams behind the club name" style="left:38px;top:1464px;width:482px;height:270px;background:radial-gradient(circle at 50% 45%,#c84cc8 0%,#7a1f8e 45%,#3a1460 100%)"></div>
    <div class="a bebas gold center" style="left:38px;top:1495px;width:482px;font-size:25px">EXCLUSIVE AND FREE – BECOME A MEMBER OF</div>
    <div class="a bebas gold center" style="left:38px;top:1552px;width:482px;font-size:66px;line-height:62px">WOLKEN UND BRISE<br>CLUB</div>
  </section>

  <!-- PAGE 3: membership, FAQ, footer -->
  <section class="page" style="left:1320px">
    <div class="a band" style="left:16px;top:0;width:524px;height:1323px"></div>
    <div class="a" style="left:16px;top:1323px;width:524px;height:426px;background:var(--navy)"></div>
    <h3 class="a bebas gold center" style="left:16px;top:47px;width:524px;font-size:21px">BENEFITS OF MEMBERSHIP:</h3>
    <div class="a" role="img" aria-label="Illustration of a magazine" style="left:92px;top:104px;width:66px;height:80px;border-radius:6px;background:linear-gradient(160deg,#f6a400,#2aa9a0)"></div>
    <div class="a" role="img" aria-label="Illustration of a drink glass" style="left:243px;top:98px;width:72px;height:74px;border-radius:50%;background:linear-gradient(160deg,#2d2350,#e23a4a)"></div>
    <div class="a" role="img" aria-label="Illustration of a discount coupon and scissors" style="left:395px;top:110px;width:72px;height:66px;border-radius:6px;background:linear-gradient(160deg,#3ad0e6,#7c3aa8)"></div>
    <div class="a white" style="left:58px;top:190px;width:131px;height:25px;background:#a9178a;font-size:7.5px;font-weight:500;display:flex;align-items:center;padding-left:9px">FREE WOLKEN &amp; BRISE MAGAZINE</div>
    <div class="a white" style="left:213px;top:186px;width:130px;height:29px;background:#a9178a;font-size:7.5px;line-height:9px;font-weight:500;display:flex;align-items:center;padding-left:8px">RECEIVE A COMPLIMENTARY DRINK<br>DURING YOUR NEXT VISIT</div>
    <div class="a white" style="left:366px;top:190px;width:130px;height:25px;background:#a9178a;font-size:7.5px;font-weight:500;display:flex;align-items:center;padding-left:8px">ACCESS TO SPECIAL DISCOUNTS</div>

    <div class="a photo" role="img" aria-label="Audience in red theatre seats" style="left:37px;top:266px;width:482px;height:283px;background:linear-gradient(135deg,#c8102e 0%,#2a1a20 20%,#241a1e 75%,#c8102e 100%)"></div>
    <h2 class="a bebas white" style="left:88px;top:298px;font-size:58px">ENJOY MORE</h2>
    <p class="a white" style="left:88px;top:355px;width:310px;font-size:21px;line-height:26px;font-weight:300">Expand your unforgettable experience – dinner options, after-show packages, and hotel stays available.</p>
    <div class="a btn-outline" style="left:312px;top:479px;width:118px;height:34px;font-size:12px">PLAN YOUR EXPERIENCE <svg viewBox="0 0 14 8"><path d="M0 4h13M10 1l3 3-3 3" stroke="currentColor" fill="none"/></svg></div>
    <svg class="a" style="left:117px;top:486px" width="60" height="60" viewBox="0 0 60 60"><circle class="ring" cx="30" cy="30" r="24"/></svg>

    <h3 class="a white" style="left:35px;top:588px;font-family:'Montserrat',sans-serif;font-weight:700;font-size:19px">FAQ – TICKETING AND SERVICE INFORMATION</h3>
    <div class="a faq-row open" style="top:623px">WHEN DOES THE BOX OFFICE OPEN? <svg viewBox="0 0 7 5"><path d="M1 4l2.5-3L6 4" stroke="#fff" fill="none"/></svg></div>
    <p class="a white" style="left:44px;top:673px;width:470px;font-size:8.5px;line-height:14px;font-weight:300">This question seeks to understand the role and scope of business consulting. Consultants typically offer a range of services including strategic planning, organizational development, operational improvement, financial analysis, and market research, among others.</p>
    <div class="a faq-row" style="top:723px">HOW DO I CONTACT THE TICKET HOTLINE? <svg viewBox="0 0 7 5"><path d="M1 1l2.5 3L6 1" stroke="#fcb900" fill="none"/></svg></div>
    <div class="a faq-row" style="top:771px">WHAT IS THE SOCIAL TICKET? WHO CAN USE IT? <svg viewBox="0 0 7 5"><path d="M1 1l2.5 3L6 1" stroke="#fcb900" fill="none"/></svg></div>
    <div class="a faq-row" style="top:819px">WHAT DISCOUNTS ARE AVAILABLE? <svg viewBox="0 0 7 5"><path d="M1 1l2.5 3L6 1" stroke="#fcb900" fill="none"/></svg></div>
    <div class="a faq-row" style="top:867px">HOW DO I BOOK WHEELCHAIR-ACCESSIBLE SEATS? <svg viewBox="0 0 7 5"><path d="M1 1l2.5 3L6 1" stroke="#fcb900" fill="none"/></svg></div>

    <h3 class="a bebas white center" style="left:16px;top:938px;width:524px;font-size:22px">TICKET HOTLINE AND SERVICE INFORMATION</h3>
    <p class="a white center" style="left:16px;top:968px;width:524px;font-size:12.5px;line-height:17px;font-weight:300">Need help with your ticket purchase? Our service team is happy to assist you!<br>Ticket Hotline Hours: Monday–Friday from 9 AM–6 PM<br>Email Support: tickets@veltora-buehne.com</p>

    <div class="a" role="img" aria-label="Drawn city skyline with cathedral and TV tower" style="left:16px;top:1100px;width:524px;height:223px;background:linear-gradient(180deg,rgba(226,24,169,0) 0%,#8a2ad0 45%,#2a16b0 100%)"></div>

    <div class="a white center" style="left:16px;top:1383px;width:524px;font-family:'Montserrat',sans-serif;font-weight:700;font-size:7.5px">Subscribe to our Newsletter</div>
    <div class="a white center" style="left:228px;top:1396px;width:100px;font-family:'Montserrat',sans-serif;font-size:4.5px;line-height:6px">Stay up-to-date! Sign up for our newsletter to never miss offers or news.</div>
    <div class="a" style="left:193px;top:1418px;width:170px;height:22px;background:var(--white);border-radius:2px"></div>
    <div class="a" style="left:201px;top:1425px;font-family:'Montserrat',sans-serif;font-size:5px;color:var(--grey)">Your email address here</div>
    <div class="a white" style="left:309px;top:1421px;width:51px;height:16px;background:var(--navy);font-family:'Montserrat',sans-serif;font-size:5.5px;display:flex;align-items:center;justify-content:center">Subscribe</div>

    <svg class="a f-icon" style="left:74px;top:1483px" viewBox="0 0 14 14"><path d="M3 1h3l1 3-2 1a7 7 0 0 0 4 4l1-2 3 1v3a1 1 0 0 1-1 1A11 11 0 0 1 2 2a1 1 0 0 1 1-1z"/></svg>
    <div class="a f-label" style="left:100px;top:1478px">Contact</div>
    <div class="a f-value" style="left:100px;top:1491px">(123) 555-0147</div>
    <svg class="a f-icon" style="left:74px;top:1522px" viewBox="0 0 14 14"><rect x="1" y="3" width="12" height="8"/><path d="M1 3l6 5 6-5"/></svg>
    <div class="a f-label" style="left:100px;top:1517px">E-mail</div>
    <div class="a f-value" style="left:100px;top:1530px">lukas.brandt@veltora-buehne</div>
    <svg class="a f-icon" style="left:74px;top:1561px" viewBox="0 0 14 14"><path d="M7 13s5-5 5-8a5 5 0 0 0-10 0c0 3 5 8 5 8z"/><circle cx="7" cy="5" r="1.8"/></svg>
    <div class="a f-label" style="left:100px;top:1556px">Address</div>
    <div class="a f-value" style="left:100px;top:1569px">Brisewald, Lindenau</div>
    <svg class="a f-icon" style="left:74px;top:1600px" viewBox="0 0 14 14"><circle cx="7" cy="7" r="6"/><path d="M7 3v4l3 2"/></svg>
    <div class="a f-label" style="left:100px;top:1595px">Opening Hours</div>
    <div class="a f-value" style="left:100px;top:1608px">1800 - 2300</div>
    <svg class="a" style="left:74px;top:1637px" width="56" height="10" viewBox="0 0 56 10"><circle cx="5" cy="5" r="4" fill="#fff"/><circle cx="20" cy="5" r="4" fill="#fff"/><circle cx="35" cy="5" r="4" fill="#fff"/><circle cx="50" cy="5" r="4" fill="#fff"/></svg>

    <div class="a f-links" style="left:294px;top:1478px"><b>Quick Links</b>Home<br>Our Services<br>About Us<br>Contact</div>
    <div class="a f-links" style="left:356px;top:1478px"><b>Legal</b>Imprint<br>Terms &amp; Conditions<br>Privacy Policy<br>Cookies</div>
    <div class="a" style="left:73px;top:1685px;width:410px;border-top:1px solid rgba(255,255,255,.35)"></div>
    <div class="a white center" style="left:16px;top:1726px;width:524px;font-family:'Montserrat',sans-serif;font-weight:700;font-size:6.5px">Copyright © 2025 Wolken und Brise - All Rights Reserved</div>
  </section>
</div>
</body>
</html>
```